Mavro Scrub - Contact/Landing Page

I need a landing page which will essentially be the page that customers will go to from the 'website' link on GMB listing. It will provide a short overview of services which need to be selectable. a little further down can capture some contact details followed by a large Submit Now button etc...

I have some icon/logo's that can be utilised at the bottom of the page as industry type references.

Target Market(s)

End of Lease Cleaning Services

Industry/Entity Type

Cleaning Service

Colors

Designer to choose colors to be used in the design.

Requirements
Must have
• As per description
Should not have
• Colours to match my website mavroscrub.com.au

```html
<!DOCTYPE html>
<html lang="en">
<head>
<meta charset="utf-8">
<title>Mavro Scrub – End of Lease Cleaning</title>
<link href="https://fonts.googleapis.com/css2?family=Libre+Caslon+Text:wght@400;700&family=Lato:wght@400;700&display=swap" rel="stylesheet">
<style>
  :root{
    --brand-blue:#1479c2;
    --brand-blue-light:#2fb2e8;
    --panel-grey:#f4f4f4;
    --band-grey:#f7f7f7;
    --ink:#111;
    --white:#fff;
    --footer:#1a1a1a;
    --serif:"Libre Caslon Text", Georgia, serif;
    --sans:"Lato", Arial, sans-serif;
  }
  *{box-sizing:border-box;margin:0;padding:0}
  html,body{width:725px;height:1200px;overflow:hidden;background:var(--white);font-family:var(--sans);color:var(--ink)}
  .page{position:relative;width:725px;height:1200px}

  .hero{position:absolute;left:0;top:0;width:725px;height:408px;background:var(--brand-blue);text-align:center;color:var(--white)}
  .brand{position:absolute;left:0;right:0;top:150px;display:flex;align-items:center;justify-content:center;gap:14px}
  .brand-dot{width:34px;height:34px;border-radius:50%;background:var(--brand-blue-light)}
  .brand-name{font-family:var(--serif);font-weight:700;font-size:48px;line-height:1;color:var(--white)}
  .tagline{position:absolute;left:0;right:0;top:327px;font-family:var(--serif);font-weight:700;font-size:18px;letter-spacing:-.2px}
  .tagline .sep{margin:0 8px;font-weight:400}

  .services{position:absolute;left:0;top:408px;width:725px;height:281px;display:flex}
  .service{width:241.67px;height:281px;background:var(--panel-grey);text-align:center;padding-top:6px}
  .service.is-featured{background:var(--brand-blue);color:var(--white)}
  .service-photo{display:block;width:232px;height:137px;margin:0 auto}
  .service-title{font-family:var(--serif);font-weight:400;font-size:15px;margin-top:21px;letter-spacing:-.2px}
  .service-desc{font-size:9px;line-height:14px;margin:9px auto 0;width:185px;height:30px}
  .select-btn{display:inline-flex;align-items:center;justify-content:center;gap:6px;margin-top:10px;width:72px;height:25px;border:1px solid var(--ink);background:var(--white);font-family:var(--serif);font-weight:700;font-size:11px;color:var(--ink)}
  .select-btn svg{width:9px;height:9px}

  .contact-form .field-label{position:absolute;left:60px;width:102px;text-align:right;font-family:var(--serif);font-weight:700;font-size:11px;line-height:29px}
  .contact-form .field-input{position:absolute;left:169px;width:213px;height:29px;border:1px solid var(--ink);border-radius:2px;background:var(--white)}
  .submit-box{position:absolute;left:424px;top:780px;width:197px;height:72px;border:1px solid var(--ink);border-radius:2px;text-align:center}
  .submit-email{font-size:10px;margin-top:7px;color:#333}
  .submit-btn{display:block;margin:6px auto 0;width:125px;height:36px;background:var(--brand-blue);border-radius:2px;color:var(--white);font-family:var(--serif);font-size:16px;line-height:36px}

  .partners{position:absolute;left:0;top:950px;width:725px;height:106px;background:var(--band-grey)}
  .partner{position:absolute;top:31px;height:44px;border-radius:3px}
  .arrow{position:absolute;top:42px;width:12px;height:20px}

  .footer{position:absolute;left:0;top:1056px;width:725px;height:144px;background:var(--footer);color:var(--white)}
  .social{position:absolute;top:40px;width:27px;height:27px;border-radius:50%;background:var(--white)}
  .copyright{position:absolute;left:0;right:0;top:104px;text-align:center;font-size:10px;letter-spacing:.2px}
  .code{position:absolute;left:657px;top:104px;font-size:10px}
</style>
</head>
<body>
<div class="page">

  <header class="hero">
    <div class="brand">
      <span class="brand-dot"></span>
      <span class="brand-name">Mavro Scrub</span>
    </div>
    <p class="tagline">End of Lease Cleaning<span class="sep">|</span>Licensed Pest Control</p>
  </header>

  <section class="services">
    <article class="service">
      <div class="service-photo" role="img" aria-label="Cleaner in gloves wiping a desk and keyboard" style="background:linear-gradient(135deg,#c9c4bb,#8a8f92 55%,#b69a74)"></div>
      <h2 class="service-title">CLEANING</h2>
      <p class="service-desc">All interior cleaning carried out to property management requirements</p>
      <span class="select-btn"><svg viewBox="0 0 10 10"><rect x=".5" y=".5" width="9" height="9" fill="none" stroke="#111"/><path d="M2.5 5l2 2 3-4" fill="none" stroke="#111" stroke-width="1.2"/></svg>Select</span>
    </article>
    <article class="service is-featured">
      <div class="service-photo" role="img" aria-label="Worker in blue gloves steam cleaning a carpet" style="background:linear-gradient(135deg,#9a8e80,#2b4f9e 45%,#c9c0b2)"></div>
      <h2 class="service-title">CARPET CLEANING</h2>
      <p class="service-desc">Carpet steam cleaning to australian standard as 3733:1995</p>
      <span class="select-btn"><svg viewBox="0 0 10 10"><rect x=".5" y=".5" width="9" height="9" fill="none" stroke="#111"/></svg>Select</span>
    </article>
    <article class="service">
      <div class="service-photo" role="img" aria-label="Pest control technicians in protective suits spraying indoors" style="background:linear-gradient(135deg,#d8d9dc,#b9bcc2 50%,#6b4430)"></div>
      <h2 class="service-title">PEST CONTROL</h2>
      <p class="service-desc">Mandatory requirement for pets on premises</p>
      <span class="select-btn"><svg viewBox="0 0 10 10"><rect x=".5" y=".5" width="9" height="9" fill="none" stroke="#111"/></svg>Select</span>
    </article>
  </section>

  <form class="contact-form">
    <label class="field-label" style="top:729px">First Name:</label><span class="field-input" style="top:729px"></span>
    <label class="field-label" style="top:765px">Surname:</label><span class="field-input" style="top:765px"></span>
    <label class="field-label" style="top:802px">Email:</label><span class="field-input" style="top:802px"></span>
    <label class="field-label" style="top:838px">Phone:</label><span class="field-input" style="top:838px"></span>
    <label class="field-label" style="top:875px">Suburb:</label><span class="field-input" style="top:875px"></span>
    <div class="submit-box">
      <p class="submit-email">info@mavroscrub.com.au</p>
      <span class="submit-btn">SUBMIT</span>
    </div>
  </form>

  <section class="partners">
    <svg class="arrow" style="left:45px" viewBox="0 0 12 20"><path d="M10 1L2 10l8 9" fill="none" stroke="#222" stroke-width="1.2"/></svg>
    <span class="partner" style="left:105px;width:87px;background:#1b1b1b"></span>
    <span class="partner" style="left:223px;width:122px;background:#d3d9ea"></span>
    <span class="partner" style="left:376px;width:67px;background:#1f4aa6"></span>
    <span class="partner" style="left:465px;width:154px;background:#7cb83a"></span>
    <svg class="arrow" style="left:660px" viewBox="0 0 12 20"><path d="M2 1l8 9-8 9" fill="none" stroke="#222" stroke-width="1.2"/></svg>
  </section>

  <footer class="footer">
    <span class="social" style="left:262px"></span>
    <span class="social" style="left:306px"></span>
    <span class="social" style="left:349px"></span>
    <span class="social" style="left:393px"></span>
    <span class="social" style="left:436px"></span>
    <p class="copyright">Copyrights @ 2021 Mavroscrub. All Rights Reserved.</p>
    <span class="code">C20</span>
  </footer>

</div>
</body>
</html>
```